Business Card Design Project

"Crest Ledger Systems" is database management company working in the direct marketing & digital printing industries. Currently going through a name & rebranding process we require a new company business card.

Industry/Entity Type

Marketing

```html
<!DOCTYPE html>
<html lang="en">
<head>
<meta charset="utf-8">
<title>Crest Ledger Systems – Business Card</title>
<link href="https://fonts.googleapis.com/css2?family=Ubuntu+Condensed&display=swap" rel="stylesheet">
<style>
  :root {
    --stage: #e6e7e9;
    --card-light: #ffffff;
    --card-light-edge: #eef0f2;
    --card-dark-top: #5a5d62;
    --card-dark-bottom: #2b2d31;
    --slate: #3f4a56;
    --ink: #3a3f46;
    --muted: #5c636b;
    --blue: #1f8fd6;
    --white: #ffffff;
  }
  * { margin: 0; padding: 0; box-sizing: border-box; }
  html, body {
    width: 1200px; height: 960px; overflow: hidden;
    background: var(--stage);
    font-family: "Ubuntu Condensed", "Arial Narrow", sans-serif;
  }
  .stage {
    position: relative; width: 1200px; height: 960px;
    display: flex; flex-direction: column; align-items: center; justify-content: center; gap: 60px;
  }
  .card {
    position: relative; width: 600px; height: 343px;
    border-radius: 22px; overflow: hidden;
    box-shadow: 0 10px 28px rgba(0,0,0,0.18);
  }
  /* Front */
  .card-front {
    background: linear-gradient(135deg, var(--card-light) 60%, var(--card-light-edge));
    color: var(--ink);
  }
  .card-front .website {
    position: absolute; top: 24px; right: 40px;
    font-size: 16px; color: var(--muted);
  }
  .brand {
    position: absolute; top: 58px; left: 48px;
    display: flex; align-items: center; gap: 12px;
    white-space: nowrap;
  }
  .brand-mark {
    width: 22px; height: 22px; background: var(--blue); border-radius: 3px; flex: none;
  }
  .brand-name {
    font-size: 34px; font-weight: 400; color: var(--slate); line-height: 1;
  }
  .person { position: absolute; left: 80px; bottom: 124px; white-space: nowrap; }
  .person-name { font-size: 30px; font-weight: 400; color: var(--ink); line-height: 1.1; }
  .person-title { font-size: 20px; font-weight: 400; color: var(--blue); margin-left: 8px; line-height: 1.1; }
  .contact {
    position: absolute; left: 60px; bottom: 24px;
    list-style: none; font-size: 18px; color: var(--muted); line-height: 1.22;
    white-space: nowrap;
  }
  .contact li { display: flex; align-items: flex-start; gap: 10px; }
  .contact .icon { width: 16px; height: 16px; flex: none; margin-top: 3px; }
  .contact .icon-at { color: var(--blue); font-size: 17px; width: 16px; text-align: center; margin-top: 0; }
  /* Back */
  .card-back {
    background: linear-gradient(160deg, var(--card-dark-top), var(--card-dark-bottom) 70%);
  }
  .card-back .brand {
    top: auto; left: auto; right: 48px; bottom: 120px;
  }
  .card-back .brand-name { color: var(--white); font-size: 36px; }
</style>
</head>
<body>
<main class="stage">
  <section class="card card-front" aria-label="Business card front">
    <p class="website">crestledger.com</p>
    <div class="brand">
      <span class="brand-mark"></span>
      <span class="brand-name">Crest Ledger Systems</span>
    </div>
    <div class="person">
      <h1 class="person-name">Owen Hartley</h1>
      <p class="person-title">PRESIDENT</p>
    </div>
    <ul class="contact">
      <li><span class="icon icon-at">@</span>owen@crestledger.com</li>
      <li>
        <svg class="icon" viewBox="0 0 18 18"><path fill="#1f8fd6" d="M4 1.5h3l1.3 4-2 1.4a10 10 0 0 0 4.8 4.8l1.4-2 4 1.3v3c0 .8-.7 1.5-1.5 1.5C7.6 15.5 2.5 10.4 2.5 3c0-.8.7-1.5 1.5-1.5z"/></svg>
        (555) 014-2290
      </li>
      <li>
        <svg class="icon" viewBox="0 0 18 18"><path fill="#1f8fd6" d="M9 1.5 1.5 8h2.2v8h4v-5h2.6v5h4V8h2.2z"/></svg>
        <span>Your Office, Your Building,<br>Street, City 12345 Country</span>
      </li>
    </ul>
  </section>

  <section class="card card-back" aria-label="Business card back">
    <div class="brand">
      <span class="brand-mark"></span>
      <span class="brand-name">Crest Ledger Systems</span>
    </div>
  </section>
</main>
</body>
</html>
```